Business card for STEADYWAVE

Please design professional business card for IT consulting firm STEADYWAVE INC.
Use logo attached.
Use information from sample qNode business card attached.
replace qnode inc with STEADYWAVE INC.
as well as qnodeinc.com with steadywave.example

```html
<!DOCTYPE html>
<html lang="en">
<head>
<meta charset="utf-8">
<title>STEADYWAVE – Business Card</title>
<link rel="stylesheet" href="https://fonts.googleapis.com/css2?family=Montserrat:wght@400;500;700;800&display=swap">
<style>
  :root {
    --page-bg: #ecebef;
    --card-white: #ffffff;
    --ink: #111111;
    --text-grey: #555559;
    --accent-purple: #8a12e0;
    --grad-start: #8a1ef0;
    --grad-mid: #7a6ae8;
    --grad-end: #3fd2f5;
  }
  * { box-sizing: border-box; margin: 0; padding: 0; }
  html, body {
    width: 1200px; height: 900px; overflow: hidden;
    background: var(--page-bg);
    font-family: "Montserrat", Arial, sans-serif;
  }
  .canvas {
    position: relative; width: 1200px; height: 900px;
  }
  .card {
    position: absolute; left: 300px; width: 600px; height: 343px;
    border-radius: 22px;
    box-shadow: 0 10px 28px rgba(0,0,0,0.16);
    overflow: hidden;
  }
  /* Front */
  .card-front {
    top: 92px;
    background: linear-gradient(135deg, var(--grad-start) 0%, var(--grad-mid) 50%, var(--grad-end) 100%);
    display: flex; align-items: center; justify-content: center;
  }
  .front-wordmark {
    color: #ffffff; font-weight: 700; font-size: 54px; letter-spacing: 8px;
    display: flex; align-items: center; gap: 16px;
  }
  .front-wordmark .mark-square {
    width: 22px; height: 22px; background: #ffffff;
  }
  /* Back */
  .card-back {
    top: 465px; background: var(--card-white);
  }
  .back-wordmark {
    position: absolute; left: 38px; top: 152px;
    color: var(--ink); font-weight: 700; font-size: 30px; letter-spacing: 3px;
    display: flex; align-items: center; gap: 10px;
  }
  .back-wordmark .mark-square {
    width: 13px; height: 13px; background: var(--accent-purple);
  }
  .divider {
    position: absolute; left: 352px; top: 92px; width: 1.5px; height: 160px;
    background: var(--accent-purple);
  }
  .contact {
    position: absolute; left: 372px; top: 88px; color: var(--text-grey);
    font-size: 13px; line-height: 1.45;
  }
  .contact-name {
    color: var(--accent-purple); font-weight: 700; font-size: 18px; letter-spacing: 0.5px;
    line-height: 1.15;
  }
  .contact-role { font-size: 13px; letter-spacing: 0.8px; margin-bottom: 8px; }
  .contact-address { margin-bottom: 8px; }
  .contact-line { display: flex; align-items: center; gap: 8px; }
  .contact-line svg { width: 11px; height: 11px; flex: none; }
</style>
</head>
<body>
<main class="canvas">
  <section class="card card-front">
    <div class="front-wordmark"><span>STEADYWAVE</span><span class="mark-square"></span></div>
  </section>

  <section class="card card-back">
    <div class="back-wordmark"><span>STEADYWAVE</span><span class="mark-square"></span></div>
    <div class="divider"></div>
    <div class="contact">
      <p class="contact-name">DANIEL REYES</p>
      <p class="contact-role">DIRECTOR</p>
      <p class="contact-address">2180 Harbourline Road,<br>Suite 204, Brookfield,<br>ON, Canada, Ontario</p>
      <p class="contact-line">
        <svg viewBox="0 0 24 24" fill="var(--accent-purple)"><path d="M6.6 10.8a15.1 15.1 0 0 0 6.6 6.6l2.2-2.2c.3-.3.7-.4 1-.2 1.1.4 2.3.6 3.6.6.6 0 1 .4 1 1V20c0 .6-.4 1-1 1A17 17 0 0 1 3 4c0-.6.4-1 1-1h3.5c.6 0 1 .4 1 1 0 1.3.2 2.5.6 3.6.1.3 0 .7-.2 1z"/></svg>
        +1 555-014-2290
      </p>
      <p class="contact-line">
        <svg viewBox="0 0 24 24" fill="none" stroke="var(--accent-purple)" stroke-width="2.2"><rect x="3" y="5" width="18" height="14" rx="1.5"/><path d="M3 6l9 7 9-7"/></svg>
        info@steadywave.example
      </p>
      <p class="contact-line">
        <svg viewBox="0 0 24 24" fill="none" stroke="var(--accent-purple)" stroke-width="2"><circle cx="12" cy="12" r="9"/><path d="M3 12h18M12 3c3 3 3 15 0 18M12 3c-3 3-3 15 0 18"/></svg>
        www.steadywave.example
      </p>
    </div>
  </section>
</main>
</body>
</html>
```